Etiketten-Design für Wein
Zielgruppe
Wir produzieren Wein und sind auf der Suche nach einer innovativen Weinetikette, welche sich durch unsere Weinvariationen durchziehen lässt.
Für das stehen wir ein: Nachhaltigkeit, moderne Landwirtschaft, Familienbetrieb, zukunftsorientiert, im Einklang mi der Natur, Freude an Pflanzen und Tieren.
Was uns gefällt: Relief / Prägung, eher schlichte, moderne und edle Etiketten, allenfalls Elemente aus der Natur, die auf Nachhaltigkeit hinweisen
Das möchten wir nicht auf der Etikette: zu knallige Farben, Comicfiguren oder ähnliches.
Unsere Weine werden direkt vermarktet und sollen aufgrund ihrer Etikette aus dem Weinregal herausstechen und ein Eyecatcher für die Kund:innen sein. Auch in einem Restaurant sollen sie als edlen Wein präsentiert werden können. Wir möchten, dass die Weinetiketten ein Storytelling mit sich bringen in Bezug auf die obenstehenden Punkte, für die wir einstehen.
Unsere Zielgruppe: Qualitätsbewusste Weingeniesser, mittleren und jüngeren Alters
Aufgabenstellung
Folgende Angaben sind auf der Etikette erforderlich:
- Weinsorte: Reserva / Riesling / Blauburgunder / Federweisser
- Name: Sennbachgut (kann klein und schlicht, unauffällig sein)
Unser Logo kann in Etikette aufgegriffen werden (auch in angepasster Form), ist aber nicht zwingend nötig. Das Logo ist auch eher revisionsbedürftig. ????
Folgende Masse sollte die Etikette ca. haben:
- Breite 95 mm
- Höhe 80 mm

```html
<!DOCTYPE html>
<html lang="de">
<head>
<meta charset="utf-8">
<title>Sennbachgut – Weinetikette</title>
<link rel="stylesheet" href="https://fonts.googleapis.com/css2?family=Montserrat:wght@600&family=Oswald:wght@700&display=swap">
<style>
  :root {
    --canvas: #ffffff;
    --label-black: #231f20;
    --green-deep: #3f7a3f;
    --green-light: #7dbb6f;
    --gold-dark: #6e4217;
    --gold-mid: #c79a5a;
    --gold-light: #f6e3bd;
    --peach: #f3c9a8;
    --text-light: #ffffff;
    --vine-green: #6dbf6a;
  }
  html, body {
    margin: 0;
    padding: 0;
    width: 1200px;
    height: 1117px;
    overflow: hidden;
    background: var(--canvas);
  }
  .canvas {
    position: relative;
    width: 1200px;
    height: 1117px;
  }
  .wine-label {
    position: absolute;
    left: 50px;
    top: 96px;
    width: 1100px;
    height: 925px;
    display: block;
  }
  .estate-place {
    font-family: "Montserrat", sans-serif;
    font-weight: 600;
    fill: var(--peach);
    letter-spacing: 6px;
  }
  .estate-name {
    font-family: "Oswald", sans-serif;
    font-weight: 700;
    fill: var(--text-light);
  }
  .variety {
    font-family: "Montserrat", sans-serif;
    font-weight: 600;
    fill: var(--text-light);
    letter-spacing: 2px;
  }
  .net-weight {
    font-family: "Montserrat", sans-serif;
    font-weight: 600;
    fill: var(--text-light);
  }
</style>
</head>
<body>
<main class="canvas">
  <svg class="wine-label" viewBox="0 0 1008 848" xmlns="http://www.w3.org/2000/svg" aria-label="Weinetikette Sennbachgut">
    <defs>
      <linearGradient id="greenSheen" x1="0" x2="1" y1="0" y2="0">
        <stop offset="0" stop-color="var(--green-deep)"/>
        <stop offset="0.5" stop-color="var(--green-light)"/>
        <stop offset="1" stop-color="var(--green-deep)"/>
      </linearGradient>
      <linearGradient id="goldBand" x1="0" x2="1" y1="0" y2="0">
        <stop offset="0" stop-color="var(--gold-mid)"/>
        <stop offset="0.3" stop-color="var(--gold-dark)"/>
        <stop offset="0.7" stop-color="var(--gold-light)"/>
        <stop offset="1" stop-color="var(--gold-mid)"/>
      </linearGradient>
      <linearGradient id="goldRule" x1="0" x2="1" y1="0" y2="0">
        <stop offset="0" stop-color="var(--gold-mid)" stop-opacity="0"/>
        <stop offset="0.35" stop-color="var(--gold-dark)"/>
        <stop offset="0.75" stop-color="var(--gold-light)"/>
        <stop offset="1" stop-color="var(--gold-mid)"/>
      </linearGradient>
      <linearGradient id="goldRuleRight" x1="0" x2="1" y1="0" y2="0">
        <stop offset="0" stop-color="var(--gold-mid)"/>
        <stop offset="0.3" stop-color="var(--gold-dark)"/>
        <stop offset="0.65" stop-color="var(--gold-light)"/>
        <stop offset="1" stop-color="var(--gold-mid)" stop-opacity="0"/>
      </linearGradient>
    </defs>

    <!-- label body -->
    <rect class="label-body" x="0" y="0" width="1008" height="848" fill="var(--label-black)"/>
    <rect class="top-band" x="0" y="0" width="1008" height="217" fill="url(#greenSheen)"/>
    <rect class="bottom-band" x="0" y="821" width="1008" height="27" fill="url(#greenSheen)"/>

    <!-- crown arch -->
    <path class="crown-arch" d="M185 217 A319 212 0 0 1 823 217 Z" fill="url(#goldBand)"/>
    <path class="crown-inner" d="M245 232 A260 190 0 0 1 765 232 L1008 232 L1008 217 L0 217 L0 232 Z" fill="var(--label-black)"/>
    <path class="crown-line" d="M0 232 L245 232 A260 190 0 0 1 765 232 L1008 232" fill="none" stroke="var(--gold-mid)" stroke-width="2"/>
    <path class="crown-fine-line" d="M262 225 A242 176 0 0 1 746 225" fill="none" stroke="var(--gold-light)" stroke-width="1" opacity="0.7"/>

    <!-- estate name -->
    <text class="estate-place" x="504" y="118" text-anchor="middle" font-size="24">TALBRUNN</text>
    <text class="estate-name" x="504" y="200" text-anchor="middle" font-size="62" textLength="330" lengthAdjust="spacingAndGlyphs">SENNBACHGUT</text>

    <!-- vine ornament area -->
    <rect class="vine-ornament" x="253" y="215" width="502" height="95" rx="40" fill="var(--vine-green)" opacity="0.35" role="img" aria-label="Weinranken-Ornament mit Traube"/>

    <!-- variety list -->
    <g class="variety-rules">
      <rect x="68" y="345" width="405" height="4" fill="url(#goldRule)"/>
      <rect x="535" y="345" width="405" height="4" fill="url(#goldRuleRight)"/>
      <rect x="68" y="438" width="405" height="4" fill="url(#goldRule)"/>
      <rect x="535" y="438" width="405" height="4" fill="url(#goldRuleRight)"/>
      <rect x="68" y="530" width="405" height="4" fill="url(#goldRule)"/>
      <rect x="535" y="530" width="405" height="4" fill="url(#goldRuleRight)"/>
      <rect x="68" y="623" width="405" height="4" fill="url(#goldRule)"/>
      <rect x="535" y="623" width="405" height="4" fill="url(#goldRuleRight)"/>
    </g>
    <g class="grape-marks" fill="var(--peach)">
      <ellipse cx="504" cy="347" rx="14" ry="17" role="img" aria-label="Traubensymbol"/>
      <ellipse cx="504" cy="440" rx="14" ry="17" role="img" aria-label="Traubensymbol"/>
      <ellipse cx="504" cy="532" rx="14" ry="17" role="img" aria-label="Traubensymbol"/>
      <ellipse cx="504" cy="625" rx="14" ry="17" role="img" aria-label="Traubensymbol"/>
    </g>
    <text class="variety" x="504" y="403" text-anchor="middle" font-size="38" textLength="222">RESERVA</text>
    <text class="variety" x="504" y="496" text-anchor="middle" font-size="38" textLength="224">RIESLING</text>
    <text class="variety" x="504" y="589" text-anchor="middle" font-size="38" textLength="442">BLAUBURGUNDER</text>
    <text class="variety" x="504" y="683" text-anchor="middle" font-size="38" textLength="380">FEDERWEISSER</text>

    <!-- base arch -->
    <path class="base-arch" d="M318 821 A186 120 0 0 1 690 821 Z" fill="url(#goldBand)"/>
    <path class="base-inner" d="M345 821 A159 92 0 0 1 663 821 Z" fill="url(#greenSheen)"/>
    <text class="net-weight" x="504" y="802" text-anchor="middle" font-size="27">NET WT 75g</text>
  </svg>
</main>
</body>
</html>
```